VKT other templates

1) Internal pages for the documents that we write. basically what will the pages inside look like. It should basically be a document with a header, a footer and a page number locator. It should include the following information: name of the report, date, VKT logo somehow, and version (draft, final etc). the information should be divided between header and footer. let me know if its unclear. As with everything it should work both in black and white and in color in case it is printed in black and white :-)
2) chapter dividers. This are the pages that you might have inside the report to separate sections. It should just have a page number, and chapter or section name. Simple, but again follow the same idea of the design that you created. It should be possible to have a picture in the divider, but it should not be a must. so in that sense we need to versions.
3) Business cards. Should include space for name, title, phone numbers (2 or 3), email, Skype, web page, and the company address which you have already.
4) a signature for emails. Basically the file that is glued to the bottom off all emails as a signature. Again it should include all the information in the business cards.

Not including any files since you have already designed others

```html
<!DOCTYPE html>
<html lang="en">
<head>
<meta charset="utf-8">
<title>VKT business card</title>
<link href="https://fonts.googleapis.com/css2?family=Exo+2:wght@400;500;700&display=swap" rel="stylesheet">
<style>
  :root {
    --backdrop: #cfdce2;
    --card-white: #ffffff;
    --sky: #7cc3e3;
    --sky-light: #a9d8ee;
    --navy: #2b3a93;
    --brand-blue: #3a73c4;
    --ink: #5b6168;
    --ink-soft: #8a9097;
    --wave: #d6e5f0;
  }
  * { margin: 0; padding: 0; box-sizing: border-box; }
  html, body { width: 1200px; height: 1000px; overflow: hidden; }
  body {
    background: var(--backdrop);
    font-family: "Exo 2", sans-serif;
    position: relative;
  }
  .card {
    position: absolute;
    width: 500px;
    height: 300px;
    overflow: hidden;
    box-shadow: 0 2px 4px rgba(40, 60, 70, 0.25);
  }
  .card-front {
    left: 90px;
    top: 200px;
    background: var(--sky);
  }
  .card-back {
    left: 610px;
    top: 500px;
    background: var(--card-white);
  }
  .front-decor {
    position: absolute;
    inset: 0;
    background: linear-gradient(160deg, rgba(255, 255, 255, 0) 45%, rgba(169, 216, 238, 0.45) 100%);
  }
  .back-decor {
    position: absolute;
    left: 0;
    right: 0;
    bottom: 0;
    height: 120px;
    background: linear-gradient(180deg, rgba(214, 229, 240, 0) 0%, var(--wave) 100%);
  }
  .front-name {
    position: absolute;
    left: 0; right: 0; top: 104px;
    text-align: center;
    color: var(--card-white);
    font-size: 84px;
    font-weight: 700;
    letter-spacing: 4px;
    line-height: 1;
  }
  .company-block {
    position: absolute;
    right: 28px;
    top: 24px;
    text-align: right;
  }
  .company-mark {
    color: var(--navy);
    font-size: 40px;
    font-weight: 700;
    letter-spacing: 2px;
    line-height: 1;
  }
  .company-name {
    color: var(--brand-blue);
    font-size: 8.5px;
    margin-top: 4px;
  }
  .company-address {
    color: var(--ink);
    font-size: 9.5px;
    line-height: 1.3;
  }
  .person {
    position: absolute;
    right: 28px;
    top: 128px;
    text-align: right;
    color: var(--ink);
  }
  .person-name { font-size: 16px; font-weight: 500; }
  .person-title { font-size: 13px; margin-top: 2px; }
  .contacts {
    position: absolute;
    right: 28px;
    top: 186px;
    text-align: right;
    color: var(--ink);
    font-size: 11px;
    line-height: 22px;
  }
  .contact-row { display: flex; justify-content: flex-end; align-items: center; gap: 6px; }
  .contact-row svg { width: 10px; height: 10px; flex: none; }
  .sep { color: var(--ink-soft); margin: 0 4px; }
</style>
</head>
<body>

  <section class="card card-front" aria-label="Card front">
    <div class="front-decor" role="img" aria-label="Soft flowing wave decoration across the card"></div>
    <div class="front-name">VKT</div>
  </section>

  <section class="card card-back" aria-label="Card back">
    <div class="back-decor" role="img" aria-label="Soft flowing wave decoration along the lower edge"></div>

    <div class="company-block">
      <div class="company-mark">VKT</div>
      <div class="company-name">Vestkyst Tekna Group Norway</div>
      <div class="company-address">Strandveien 18,<br>0252 Oslo, Norway</div>
    </div>

    <div class="person">
      <div class="person-name">Erik Lund</div>
      <div class="person-title">Managing Director</div>
    </div>

    <div class="contacts">
      <div class="contact-row">
        <svg viewBox="0 0 10 10" aria-hidden="true"><path d="M2 1 L4 3 L3 4 Q4 6 6 7 L7 6 L9 8 L8 9 Q4 9 1 5 Q1 2 2 1 Z" fill="var(--brand-blue)"/></svg>
        <span>+47 21550300</span><span class="sep">|</span><span>+47 21550301</span><span class="sep">|</span><span>+47 21550302</span>
      </div>
      <div class="contact-row">
        <svg viewBox="0 0 10 10" aria-hidden="true"><circle cx="5" cy="5" r="4.2" fill="none" stroke="var(--brand-blue)" stroke-width="1"/><path d="M1 5 H9 M5 1 Q2.5 5 5 9 M5 1 Q7.5 5 5 9" stroke="var(--brand-blue)" stroke-width="0.8" fill="none"/></svg>
        <span>www.vkt.no</span><span class="sep">|</span>
        <svg viewBox="0 0 10 10" aria-hidden="true"><circle cx="5" cy="5" r="4.5" fill="var(--brand-blue)"/></svg>
        <span>Erik.Lund</span>
      </div>
      <div class="contact-row">
        <svg viewBox="0 0 10 10" aria-hidden="true"><rect x="0.5" y="2" width="9" height="6" fill="var(--brand-blue)"/><path d="M0.5 2 L5 5.5 L9.5 2" stroke="#ffffff" stroke-width="0.8" fill="none"/></svg>
        <span>post@vkt.no</span>
      </div>
    </div>
  </section>

</body>
</html>
```